Wok & Roll Reimage

Hi Marlene, (FOR MARLENE ONLY !!!)

So I've just done a new photoshoot to refresh my product image. I need your help in changing all my print posters and digital menus again :)
I don't need them to be completely different, just simply new images and content. These are the details as follow:

1. Bowl-Ideal Combo: I'm thinking this does need to be completely redesign.
I like the poster to say:
- Choose Your Sides - show all side dishes
- Choose Your Mains - show all main dishes
- Choose Any Drinks FREE (From Fridge Only) Really emphasise the FREE DRINK
- NO PRICING REQUIRED

2. Menu Board - Redo the poster - Delete the Stirfry Noodle
- Add in the new side dishes
- There's also a new dish in RICE (Lemongrass Chilli Beef Rice)

3. Catering Poster : change the content as follow and new photo:
Fresh Ricepaper Rolls
30 Rolls $80
50 Rolls $135

Springrolls
30 Rolls $45
50 Rolls $75

Team Meals $20 per person
(Minimum 10 people)
1x Any Mains / 1x Any Sides / 1X Any Drinks

4. Digital Menu ( I need this first - most important )
⁃ Change title of ROLLS to SIDES. Remove the potato shrimps and add the 2 new items
⁃ Delete Stirfry Noodles from menu
⁃ Combine SIDES with NOODLE SALADS and RICE to same page
⁃ Make Pho photos bigger - new photos

1. FREE Phở COMPETITION (This is a new poster for my new snapgrid campaign)
Title : WIN FREE Phở till the end of 2019.
Content : Here's how you can WIN. Simply share your photo on Snapgrid
⁃ Take an original photo of any items on our menu (Purchased in-store or with DashBite/Platerush/Forkly)
⁃ Post your photos to Snapgrid using hashtags #freebowlcomp2019 #wokandroll
⁃ Be as creative as you'd like. The best photo voted by Wok&Roll team will WIN.
Terms & Conditions:
The competition opens from 9am Thursday 1st August and closes at 11:59pm Saturday 28th September 2019.
The winner will be announce on Monday 30th September 2019.
The winner will receive 1 Free Phở (or any mains on menu) per day till end of 2019.
Must collect food from Randwick store ONLY.
All entries must not have been used in previous Wok&Roll competitions and the number of entries an Eligible Entrant may send is not limited, provided each entry is different and tagged correctly. This is a game of skill. Each entry will be individually judged, based upon individual creative merits.

```html
<!DOCTYPE html>
<html lang="en">
<head>
<meta charset="utf-8">
<title>Digital Menu Board</title>
<link rel="stylesheet" href="https://fonts.googleapis.com/css2?family=Oswald:wght@500;600&family=Roboto:wght@700;900&display=swap">
<style>
  :root {
    --page: #ffffff;
    --board: #151515;
    --board-edge: #1d1d1d;
    --orange: #f47c20;
    --white: #ffffff;
    --muted: #b9b9b9;
    --pill-dark: #3a3a3a;
    --plate: #f4f4f4;
  }
  * { margin: 0; padding: 0; box-sizing: border-box; }
  html, body { width: 1200px; height: 1200px; overflow: hidden; background: var(--page); }
  .menu-board {
    position: absolute; left: 78px; top: 307px; width: 1044px; height: 585px;
    background: linear-gradient(135deg, var(--board-edge), var(--board) 60%);
    font-family: "Roboto", Arial, sans-serif; color: var(--white);
  }
  .section-title, .section-price, .item-price, .extra-label, .extra-price {
    font-family: "Oswald", "Arial Narrow", sans-serif;
  }
  .section-title {
    position: absolute; left: 49px; color: var(--orange);
    font-weight: 600; font-size: 44px; line-height: 40px; letter-spacing: 0.5px;
  }
  .section-price {
    position: absolute; left: 50px; font-weight: 600; font-size: 30px; line-height: 30px;
  }
  .divider { position: absolute; left: 47px; width: 950px; height: 2px; background: var(--orange); }
  .item { position: absolute; width: 200px; margin-left: -100px; text-align: center; }
  .item-name { font-weight: 900; font-size: 17px; line-height: 17px; letter-spacing: 0.2px; }
  .item-note { font-weight: 700; font-size: 17px; line-height: 19px; color: var(--muted); }
  .item-price { font-weight: 600; font-size: 27px; line-height: 30px; margin-top: 4px; }
  .photo { position: absolute; }
  .photo-plate {
    width: 135px; height: 95px; margin-left: -67px; border-radius: 18px;
    transform: rotate(-14deg);
    box-shadow: 0 4px 10px rgba(0,0,0,0.6);
  }
  .photo-bowl {
    width: 106px; height: 106px; margin-left: -53px; margin-top: -53px; border-radius: 50%;
    box-shadow: 0 4px 10px rgba(0,0,0,0.6);
  }
  .photo-dish {
    width: 135px; height: 82px; margin-left: -67px; margin-top: -41px; border-radius: 16px;
    transform: rotate(-18deg) skewX(-20deg);
    box-shadow: 0 4px 10px rgba(0,0,0,0.6);
  }
  .extras {
    position: absolute; left: 291px; top: 510px; width: 461px; height: 53px;
    border-radius: 27px; overflow: hidden; display: flex;
  }
  .extras-label {
    width: 93px; background: var(--pill-dark); display: flex; align-items: center; justify-content: center;
  }
  .extra-label { font-weight: 500; font-size: 22px; line-height: 21px; text-align: center; }
  .extras-list { flex: 1; background: var(--orange); display: flex; align-items: center; justify-content: space-around; padding: 0 14px 0 4px; }
  .extra { text-align: center; }
  .extra-price { display: block; font-weight: 600; font-size: 22px; line-height: 22px; }
  .extra-name { display: block; font-weight: 900; font-size: 15px; line-height: 16px; }
</style>
</head>
<body>
<main class="menu-board">

  <!-- Sides -->
  <h2 class="section-title" style="top:33px;">SIDES</h2>

  <div class="photo photo-plate" style="left:265px;top:30px;background:radial-gradient(circle at 50% 50%,#f3d7c4,#f1f1ef 70%);" role="img" aria-label="Three fresh rice paper rolls with prawns and herbs on a white plate"></div>
  <div class="photo photo-plate" style="left:465px;top:30px;background:radial-gradient(circle at 45% 55%,#d9b77e,#f3f1ee 70%);" role="img" aria-label="Four spring rolls with chilli dipping sauce on a white plate"></div>
  <div class="photo photo-plate" style="left:663px;top:30px;background:radial-gradient(circle at 50% 50%,#b99a5a,#f2f2f0 72%);" role="img" aria-label="Salt and pepper pork ribs with chilli and spring onion on a white plate"></div>
  <div class="photo photo-plate" style="left:865px;top:30px;background:radial-gradient(circle at 50% 50%,#c8a468,#f2f2f0 72%);" role="img" aria-label="Salt and pepper chicken ribs with chilli on a white plate"></div>

  <div class="item" style="left:265px;top:135px;"><p class="item-name">1. RICEPAPER<br>ROLLS (3)</p><p class="item-price">$11.00</p></div>
  <div class="item" style="left:468px;top:135px;width:220px;margin-left:-110px;"><p class="item-name">2. SPRING ROLLS (4)</p><p class="item-note">(Seafood/Vegetarian)</p><p class="item-price" style="margin-top:0;">$8.90</p></div>
  <div class="item" style="left:668px;top:135px;"><p class="item-name">3. SALT N PEPPER<br>PORK RIB</p><p class="item-price">$9.90</p></div>
  <div class="item" style="left:863px;top:135px;"><p class="item-name">4. SALT N PEPPER<br>CHICKEN RIB</p><p class="item-price">$9.90</p></div>

  <div class="divider" style="top:206px;"></div>

  <!-- Noodle salad -->
  <h2 class="section-title" style="top:227px;">NOODLE<br>SALAD</h2>
  <p class="section-price" style="top:310px;">$15.90</p>

  <div class="photo photo-bowl" style="left:271px;top:268px;background:radial-gradient(circle,#7a5a32,#8a6a3a 50%,#f3f3f3 72%);" role="img" aria-label="Lemongrass beef noodle salad bowl with herbs"></div>
  <div class="photo photo-bowl" style="left:466px;top:268px;background:radial-gradient(circle,#b8975f,#a88a55 50%,#f3f3f3 72%);" role="img" aria-label="Lemongrass chicken noodle salad bowl with herbs"></div>
  <div class="photo photo-bowl" style="left:662px;top:268px;background:radial-gradient(circle,#8a6a3c,#7d6238 50%,#f3f3f3 72%);" role="img" aria-label="BBQ pork noodle salad bowl with herbs"></div>
  <div class="photo photo-bowl" style="left:859px;top:268px;background:radial-gradient(circle,#d9a94a,#b9a458 50%,#f3f3f3 72%);" role="img" aria-label="Tofu noodle salad bowl with herbs"></div>

  <div class="item" style="left:273px;top:325px;width:220px;margin-left:-110px;"><p class="item-name">1. LEMONGRASS<br>BEEF</p></div>
  <div class="item" style="left:470px;top:325px;width:220px;margin-left:-110px;"><p class="item-name">2. LEMONGRASS<br>CHICKEN</p></div>
  <div class="item" style="left:664px;top:325px;"><p class="item-name">3. BBQ PORK</p></div>
  <div class="item" style="left:861px;top:325px;"><p class="item-name">4. TOFU</p></div>

  <div class="divider" style="top:362px;"></div>

  <!-- Rice -->
  <h2 class="section-title" style="top:377px;">RICE</h2>
  <p class="section-price" style="top:417px;">$19.90</p>

  <div class="photo photo-dish" style="left:271px;top:415px;background:radial-gradient(circle at 40% 55%,#4d6a2c,#6b4a30 40%,#f2f2f0 75%);" role="img" aria-label="BBQ beef with broccoli and carrot beside steamed rice"></div>
  <div class="photo photo-dish" style="left:437px;top:415px;background:radial-gradient(circle at 40% 55%,#7a5a38,#5d6a2e 40%,#f2f2f0 75%);" role="img" aria-label="Lemongrass chilli beef with beans beside steamed rice"></div>
  <div class="photo photo-dish" style="left:604px;top:415px;background:radial-gradient(circle at 40% 55%,#c99a45,#7a8a3a 40%,#f2f2f0 75%);" role="img" aria-label="Lemongrass chilli chicken with vegetables beside steamed rice"></div>
  <div class="photo photo-dish" style="left:767px;top:415px;background:radial-gradient(circle at 40% 55%,#4f7a30,#b58a40 40%,#f2f2f0 75%);" role="img" aria-label="Tofu and mixed vegetables beside steamed rice"></div>
  <div class="photo photo-dish" style="left:928px;top:415px;background:radial-gradient(circle at 50% 50%,#d8b880,#e3c99a 45%,#f2f2f0 75%);" role="img" aria-label="Fried rice with prawns and vegetables"></div>

  <div class="item" style="left:273px;top:468px;"><p class="item-name">1. BBQ BEEF</p></div>
  <div class="item" style="left:434px;top:468px;"><p class="item-name">2. LEMONGRASS<br>CHILLI BEEF</p></div>
  <div class="item" style="left:605px;top:468px;"><p class="item-name">2. LEMONGRASS<br>CHILLI CHICKEN</p></div>
  <div class="item" style="left:767px;top:468px;"><p class="item-name">3. TOFU &amp; VEGS</p></div>
  <div class="item" style="left:928px;top:468px;"><p class="item-name">4. FRIED RICE</p><p class="item-note">(Prawns/<br>Chicken/Tofu)</p></div>

  <!-- Add extra -->
  <div class="extras">
    <div class="extras-label"><p class="extra-label">*ADD<br>EXTRA</p></div>
    <div class="extras-list">
      <p class="extra"><span class="extra-price">$2.00</span><span class="extra-name">MEAT</span></p>
      <p class="extra"><span class="extra-price">$2.00</span><span class="extra-name">VEGETABLES</span></p>
      <p class="extra"><span class="extra-price">$2.00</span><span class="extra-name">TOFU</span></p>
      <p class="extra"><span class="extra-price">$1.50</span><span class="extra-name">NOODLES</span></p>
    </div>
  </div>

</main>
</body>
</html>
```